Trävana: Wedding Website & Invite Template

I'm looking for help creating my Wedding Website & stationary. I'm using Travana (www.travana-sample.com) to manage my guests/invites/information which allows you to upload your own design for the website and invites. Please see attached all the templates which I would like to be able to use. This includes:

1. Trävana Full Page (Full site background / design)
2. Trävana Header (Site header design)
3. Trämora Portrait (Invite portrait)
4. Trämora Square (invite square)
5. Logo/Monogram (That we can use on order of service & other stationary)

The idea being that I upload the design and then customise the content overlaid. When making Trävana designs, be sure that the title, links and text will be readable over the design. Trävanas get taller as content is added. So for full-page designs, we suggest patterns that can be tiled or else fade at the bottom into a solid color. This way, when you upload the design you can select a background color to match.

I would like the overall design to be simple and understated. I like shabby chic/rustic and nothing too traditional. I like hearts, lovebirds and trees. The wedding will be in a wig-wam in rural Oxfordshire, England. It'll be in the summer but will be a very informal event. If appropriate, it could include a monogram of our initials 'N&F' or first names 'Nora & Felix'. We need some sort of logo whether it includes or intials/names or not, it could just be a love heart as shown on the first design inspiration below.

1. I really like this rustic style design: https://www.craftbarn-example.com/listing/215067463/engagement-party-invitation-engagement?ref=br_feed_11&br_feed_tlp=weddings

2. https://www.craftbarn-example.com/listing/166727076/participation-and-kraft-paper-wedding?ref=br_feed_19&br_feed_tlp=weddings

3. https://www.craftbarn-example.com/listing/198265358/shabby-chic-i-do-bbq-lnvitation?ref=br_feed_42&br_feed_tlp=weddings

4. https://www.craftbarn-example.com/listing/157426460/wedding-rehearsal-dinner-invitation?ref=br_feed_56&br_feed_tlp=weddings

Target Market(s)

The majority of my guests are between the ages of 25 and 35, Male and Female, English/American/Australian.

Industry/Entity Type

Wedding

Font styles to use
Sans Serif
Script

Colors
f04a50
f59195
fbd3d4
f9ba93
fce7d3
dcdcdc
cacaca
ffffff
757575

Requirements
Must have
• It should utilise at least 1 colour out of Coral, Pink, Orange. Coral is the main colour.
Should not have
• - Fonts that are defined as 'script' i.e. swirly, old fashioned fonts.

```html
<!DOCTYPE html>
<html lang="en">
<head>
<meta charset="utf-8">
<title>Nora &amp; Felix — Wedding</title>
<link href="https://fonts.googleapis.com/css2?family=Amatic+SC:wght@400;700&family=Montserrat:wght@400;500&display=swap" rel="stylesheet">
<style>
  :root {
    --coral: #f04a50;
    --pink: #f59195;
    --blush: #fbd3d4;
    --peach: #f9ba93;
    --cream: #fce7d3;
    --paper: #f8e6cf;
    --grey: #757575;
    --line-grey: #cacaca;
    --clip: #1e1a1a;
    --orange: #f08a3c;
  }
  * { margin: 0; padding: 0; box-sizing: border-box; }
  html, body { width: 1200px; height: 1059px; overflow: hidden; }
  body { position: relative; background: #2a1208; font-family: "Montserrat", sans-serif; }

  .site-header {
    position: absolute; left: 0; top: 0; width: 1200px; height: 197px;
    background: linear-gradient(180deg, #fbead6 0%, #f6dfc4 100%);
    display: flex; align-items: center; justify-content: center; gap: 12px;
  }
  .brand-dot { width: 14px; height: 14px; border-radius: 50%; background: var(--peach); }
  .brand-name {
    font-family: "Amatic SC", sans-serif; font-weight: 700;
    font-size: 56px; line-height: 1; color: var(--coral); letter-spacing: 2px;
  }

  .forest-scene {
    position: absolute; left: 0; top: 197px; width: 1200px; height: 862px;
    background:
      radial-gradient(ellipse 380px 320px at 330px 470px, rgba(255,190,90,0.85), rgba(255,140,40,0) 70%),
      radial-gradient(ellipse 300px 260px at 1120px 320px, rgba(255,200,120,0.7), rgba(255,140,40,0) 70%),
      linear-gradient(180deg, #3a1a0c 0%, #6b2e0e 35%, #c0621c 62%, #d9822a 78%, #8a3f12 100%);
  }

  .nav-panel {
    position: absolute; left: 182px; top: 254px; width: 207px; height: 529px;
    background: var(--paper); box-shadow: 0 4px 14px rgba(0,0,0,0.35);
    padding: 68px 0 0 27px;
  }
  .nav-panel ul { list-style: none; }
  .nav-panel li {
    font-family: "Amatic SC", sans-serif; font-size: 36px; line-height: 51px;
    color: var(--coral); letter-spacing: 1px; white-space: nowrap;
  }

  .binder-clip { position: absolute; top: 197px; width: 34px; height: 60px; }
  .binder-clip.left { left: 618px; }
  .binder-clip.right { left: 890px; }

  .invite-card {
    position: absolute; left: 461px; top: 244px; width: 564px; height: 705px;
    background: var(--paper); box-shadow: 0 6px 18px rgba(0,0,0,0.4);
    text-align: center;
  }
  .bunting-string { position: absolute; left: 0; top: 30px; width: 564px; height: 20px; }
  .bunting {
    position: absolute; left: 79px; top: 38px; width: 407px; height: 45px;
    background: linear-gradient(90deg, #f3c98a, #f2b6ae, #e9c98c);
  }
  .heart-artwork {
    position: absolute; left: 85px; top: 108px; width: 380px; height: 230px;
    background: radial-gradient(ellipse 150px 120px at 50% 48%, rgba(240,74,80,0.55), rgba(245,145,149,0.15) 70%, rgba(248,230,207,0) 100%);
    display: flex; align-items: center; justify-content: center;
  }
  .heart-artwork .brand-name { font-size: 40px; background: #f9c99d; padding: 4px 22px; }

  .card-text { position: absolute; left: 0; width: 100%; white-space: nowrap; }

  .invite-title {
    top: 346px; line-height: 46px;
    font-family: "Amatic SC", sans-serif; font-weight: 400; font-size: 44px;
    color: var(--coral); letter-spacing: 2px;
  }
  .dotted { position: absolute; left: 77px; width: 410px; border-top: 4px dotted var(--coral); }
  .dotted.orange { border-top-color: var(--peach); }
  .dotted.d1 { top: 398px; }
  .dotted.d2 { top: 487px; }
  .dotted.d3 { top: 623px; }

  .invite-line { line-height: 20px; text-transform: uppercase; }
  .invite-line.grey { color: var(--grey); }
  .invite-line.coral { color: var(--coral); }
  .l1 { top: 409px; font-size: 17px; letter-spacing: 1.5px; }
  .l2 { top: 436px; font-size: 17px; letter-spacing: 0.5px; }
  .l3 { top: 460px; font-size: 15.5px; letter-spacing: 0.3px; }
  .l4 { top: 599px; font-size: 13.5px; letter-spacing: 0.8px; }

  .invite-date {
    top: 504px; line-height: 44px;
    font-family: "Amatic SC", sans-serif; font-size: 40px; color: var(--coral); letter-spacing: 1px;
  }
  .date-rule { position: absolute; top: 527px; width: 113px; border-top: 2px solid var(--line-grey); }
  .date-rule.left { left: 82px; }
  .date-rule.right { right: 82px; }
  .invite-time {
    top: 546px; line-height: 16px;
    font-family: "Amatic SC", sans-serif; font-size: 16px; color: var(--coral);
  }
  .invite-address {
    top: 568px; line-height: 20px;
    font-family: "Amatic SC", sans-serif; font-size: 19px; color: var(--orange); text-transform: uppercase;
  }
  .invite-rsvp {
    top: 632px; line-height: 24px;
    font-family: "Amatic SC", sans-serif; font-size: 21px; letter-spacing: 0.5px;
    color: var(--pink); text-transform: uppercase;
  }
</style>
</head>
<body>
  <header class="site-header">
    <span class="brand-dot"></span>
    <span class="brand-name">Nora &amp; Felix</span>
  </header>

  <div class="forest-scene" role="img" aria-label="Sunlit woodland with tall trees and golden evening grass"></div>

  <nav class="nav-panel">
    <ul>
      <li>The Wedding</li>
      <li>Location</li>
      <li>Travell</li>
      <li>Attendnce</li>
    </ul>
  </nav>

  <svg class="binder-clip left" viewBox="0 0 34 60" aria-hidden="true">
    <line x1="17" y1="0" x2="17" y2="38" stroke="#555" stroke-width="2"/>
    <path d="M4 38 H30 L27 58 H7 Z" fill="var(--clip)"/>
  </svg>
  <svg class="binder-clip right" viewBox="0 0 34 60" aria-hidden="true">
    <line x1="17" y1="0" x2="17" y2="38" stroke="#555" stroke-width="2"/>
    <path d="M4 38 H30 L27 58 H7 Z" fill="var(--clip)"/>
  </svg>

  <main class="invite-card">
    <svg class="bunting-string" viewBox="0 0 564 20" aria-hidden="true">
      <path d="M0 4 Q282 16 564 4" fill="none" stroke="#7a5a4a" stroke-width="1.5"/>
    </svg>
    <div class="bunting" role="img" aria-label="Row of colourful patterned bunting flags"></div>

    <div class="heart-artwork" role="img" aria-label="Floral heart with ribbon, small hearts and a pair of lovebirds on a branch">
      <span class="brand-name">Nora &amp; Felix</span>
    </div>

    <h1 class="card-text invite-title">NORA AND FELIX'S WEDDING</h1>
    <div class="dotted d1"></div>
    <p class="card-text invite-line grey l1">We'll be honourded and thrilled</p>
    <p class="card-text invite-line coral l2">If yu join us to celebrate our wedding</p>
    <p class="card-text invite-line grey l3">We'll appreciate you presence and support</p>
    <div class="dotted orange d2"></div>

    <div class="date-rule left"></div>
    <p class="card-text invite-date">13.05.2015</p>
    <div class="date-rule right"></div>
    <p class="card-text invite-time">5 PM</p>
    <p class="card-text invite-address">Address place, street, street &amp; city, post code</p>

    <p class="card-text invite-line grey l4">You can indulge in food drinks and party after</p>
    <div class="dotted d3"></div>
    <p class="card-text invite-rsvp">RSVP by 30 January 2015 &nbsp;at noraandfelix.travana-sample.com</p>
  </main>
</body>
</html>
```